Consulting services and software brochure

We need a brochure designed that would ideally work with our logo and highlight a few of our consulting services and a couple products we offer. Our industry is real estate technology and we focus on consulting services for third party software systems. We would like the design to work well with our logo colors although we are open to changing either the blue or the orange to white in a design. The final design should clearly highlight our service options in an easy to read way while also leaving plenty of room to insert a lot of text on each service

What we like about our current design: it incorporates our colors well and has lots of room for text on each service, the two product offerings, and a couple testimonials from our clients

What we don’t like: It’s very busy and doesn’t highlight our offerings without a lot of reading. We also think it could have better layout, be much more polished and interesting visually (this was not designed by a professional).

Please provide source file compatible with Photoshop.

We are impressed with the designs so far and have made the payment guaranteed for this project. We will be starting to provide feedback early next week as we review internally.

Regarding size: We are open to a multi-page brochure or an 8 1/2 x 11, square shape, etc. After reviewing the designs we have decided the tri-folds seem to look too busy though on a standard piece of paper. Also, there's a good chance whatever designer we choose we will also hire to do another option in a different size/length so please don't worry either way too much about that.

Thanks for the great submissions so far!

Reason: Hi - we're extending the deadline a week since a few people providing input have been out this week for Passover and Good Friday. Thank you for your understanding.

Reason: Hi - we've settled on a designer and are now refining the brochure. Thank you everyone for your time and effort.

```html
<!DOCTYPE html>
<html lang="en">
<head>
<meta charset="utf-8">
<title>Consulting Services Brochure – Inside Spread</title>
<link rel="stylesheet" href="https://fonts.googleapis.com/css2?family=Barlow:wght@500;600&family=Ubuntu:wght@400;500&display=swap">
<style>
  :root {
    --backdrop: #b4b4b4;
    --navy: #0f2038;
    --orange: #e8831d;
    --orange-deep: #d9741a;
    --heading-orange: #f08a1f;
    --paper-text: #ffffff;
    --ink: #1a1a1a;
    --photo-light: #9a9a9a;
    --photo-dark: #3c3c3c;
  }
  * { box-sizing: border-box; margin: 0; padding: 0; }
  html, body {
    width: 1200px; height: 847px; overflow: hidden;
    background: var(--backdrop);
  }
  .spread {
    position: absolute; left: 100px; top: 100px;
    width: 1000px; height: 647px;
    display: flex;
    box-shadow: 0 18px 40px rgba(0,0,0,.25);
  }
  .page { position: relative; width: 500px; height: 647px; display: flex; }

  .solutions {
    width: 300px; height: 100%;
    background: var(--navy);
    color: var(--paper-text);
    padding: 38px 24px 0 30px;
    font-family: "Ubuntu", sans-serif;
    font-size: 10.6px; line-height: 1.3;
  }
  .panel-title {
    font-family: "Barlow", sans-serif;
    font-weight: 600; font-size: 21px; line-height: 1;
    margin-bottom: 12px;
  }
  .solutions .panel-title { color: var(--heading-orange); }
  .service + .service { margin-top: 12px; }
  .service-title {
    font-family: "Barlow", sans-serif; font-weight: 600;
    font-size: 13px; color: var(--heading-orange);
    display: flex; align-items: center; gap: 6px;
  }
  .service-title::before {
    content: ""; width: 6px; height: 6px; background: var(--heading-orange);
  }

  .photo {
    flex: 1; height: 100%;
    background: radial-gradient(ellipse at 50% 45%, var(--photo-light), var(--photo-dark) 80%);
  }

  .intelligence {
    width: 100%; height: 100%;
    background: linear-gradient(90deg, var(--orange-deep), var(--orange) 12%);
    color: var(--paper-text);
    padding: 40px 44px 0 44px;
    font-family: "Ubuntu", sans-serif;
    font-size: 11.6px; line-height: 1.32;
  }
  .intelligence .panel-title { color: var(--ink); margin-bottom: 16px; }
  .intelligence p + p { margin-top: 16px; }
  .intelligence .note {
    margin-top: 18px; color: var(--ink);
    font-size: 8.5px; font-weight: 500; line-height: 1.3;
  }
</style>
</head>
<body>
  <main class="spread">
    <section class="page page-left">
      <div class="solutions">
        <h2 class="panel-title">Solutions</h2>
        <div class="service">
          <h3 class="service-title">Customization</h3>
          <p>While the real estate industry has seen great strides in recent years in the quality of the software offerings available to it, no product serves every business out of the box. Nor should it; every business is unique. At ParcelPoint we are experts at crafting an approach that begins with the best system available for an organization and molding it into a complete solution for the way you do business. Sometimes this can be accomplished through subtle setup and design decisions, other times a project calls for more broad brush changes to process flow and even look and feel. In some cases we are called upon to augment a system’s functionality with additional custom-built components that are tightly integrated with the base system.</p>
        </div>
        <div class="service">
          <h3 class="service-title">System Integration</h3>
          <p>More and more often data that is generated, stored, maintained, analyzed and displayed by disparate systems performing different functions needs to work together as one. Data must be exchanged seamlessly and meaningfully between systems on different platforms using different technology often in, or close to, real time. Systems integration is another area in which ParcelPoint with depth in real estate business process, real estate systems, and custom programming, is uniquely positioned to provide cutting edge and cost effective solutions.</p>
        </div>
      </div>
      <div class="photo" role="img" aria-label="Black and white photo of a businessman in a suit and tie holding a transparent tablet showing charts and a world map"></div>
    </section>

    <section class="page page-right">
      <div class="intelligence">
        <h2 class="panel-title">Business Intelligence</h2>
        <p>With this industry leading business intelligence solution investors are able to view potential threats ahead of time and take action. Revenues and forecasted revenues are compared to budgets and can be viewed in detail for every single lease and prospect within a few clicks.</p>
        <p>Traditionally CRM’s don’t talk to financial and accounting systems such as Stratum and Keyline. Until now there hasn’t been one platform that brings in data from multiple areas so that investors and property managers are able to see the performance of their investments in a dynamic way. Experience how to bridge the divide and provide you with actionable intelligence!</p>
        <p>Most systems spit out numbers letting you do the work of imagining what they look like. This BI tool makes your performance metrics come to life with dashboards, interactive graphs and charts. Key features include determining P&amp;L line-level trends, drilling down to GL details, and forecasting metrics based on trends! Quickly switch between trends and values to make your analysis more insightful, look at any line item and view actuals by property along with comparison, and build your own custom portfolios allowing multiple asset types!</p>
        <p class="note">* if you need more solutions to get the text to be spaced well I can provide more*</p>
      </div>
    </section>
  </main>
</body>
</html>
```